Design a corporate looking website for Harbourline Funding

Need design only WordPress mock up for Harbourline Funding who provides short term finance solutions to other businesses. We need a corporate looking website that depicts a trustworthy, Dynamic fast acting company.
Visit http://k7.pagelantern-demo.net/ for current mock up We need something like e this but not the same with a design that depicts corporate with more colour and images, needs to install trust and fast action. Please feel free to change the layout as I am not wedded to current design but am happy with what on the landing page.

Target Market(s)

Small to medium sized Businesses

Industry/Entity Type

Finance

Number of Pages Required

1 page

Font styles to use
Sans Serif

Requirements
Must have
• Design Landing pages in WordPress
• Visit http://k7.pagelantern-demo.net/ for current mock up need Layout like this but with a design that depicts corporate with more colour and images, needs to install trust and fast action. Please feel free to change the layout as I am not happy with current design but am wedded to what on the landing page.
Should not have
• any copyright material on it.

```html
<!DOCTYPE html>
<html lang="en">
<head>
<meta charset="utf-8">
<title>Harbourline Funding</title>
<link href="https://fonts.googleapis.com/css2?family=Open+Sans:wght@400;600;700;800&family=Great+Vibes&display=swap" rel="stylesheet">
<style>
:root{
  --blue:#1b8fe0;
  --blue-dark:#1470b3;
  --ink:#222;
  --muted:#6d6d6d;
  --light:#f3f3f3;
  --dark:#1b1b1b;
  --darker:#141414;
  --white:#fff;
}
*{margin:0;padding:0;box-sizing:border-box}
html,body{width:1200px;height:2688px;overflow:hidden}
body{font-family:"Open Sans",Arial,sans-serif;color:var(--ink);background:var(--white);position:relative}
section,header,footer,nav{position:absolute;left:0;width:1200px}
.abs{position:absolute}
.btn{position:absolute;background:var(--blue);color:var(--white);font-size:12px;font-weight:600;text-align:center;letter-spacing:.5px}

/* hero */
.hero{top:0;height:532px;background:linear-gradient(180deg,#3a3430 0%,#5b4c40 40%,#2c2a2a 100%)}
.hero-photo{position:absolute;inset:0;background:radial-gradient(ellipse at 50% 40%,rgba(190,160,130,.45),rgba(20,20,25,.8) 75%)}
.hero h1{position:absolute;top:360px;width:100%;text-align:center;color:var(--white);font-size:36px;font-weight:800;letter-spacing:.5px}
.hero p{position:absolute;top:410px;left:330px;width:540px;text-align:center;color:#ddd;font-size:10px;line-height:14px}
.hero .btn{top:478px;left:525px;width:150px;height:34px;line-height:34px;font-size:15px;font-weight:400;letter-spacing:1px}

/* nav */
.topnav{top:532px;height:68px;background:var(--white);border-bottom:1px solid #e5e5e5}
.brand{position:absolute;left:190px;top:22px;display:flex;align-items:center;gap:8px;font-weight:700;font-size:15px;color:var(--blue-dark)}
.brand i{width:14px;height:14px;background:var(--blue-dark);display:block}
.menu{position:absolute;left:380px;top:28px;display:flex;gap:22px;font-size:10px;color:var(--muted)}

/* about */
.about{top:600px;height:560px;background:var(--light)}
.about-person{position:absolute;left:150px;top:40px;width:320px;height:520px;background:linear-gradient(180deg,#d9d4cf,#9a9592 60%,#2f3038)}
.about h2{position:absolute;left:490px;top:64px;font-size:30px;font-weight:700;color:#333}
.about .intro{position:absolute;left:490px;top:112px;width:640px;font-size:10px;line-height:15px;color:var(--muted)}
.feature{position:absolute;width:200px}
.feature .ic{position:absolute;left:0;top:0;width:26px;height:26px;border-radius:50%;background:#555}
.feature h4{margin-left:36px;font-size:11px;font-weight:600;color:#444}
.feature p{margin-left:36px;margin-top:4px;font-size:9px;line-height:13px;color:var(--muted)}
.about-plant{position:absolute;left:880px;top:200px;width:270px;height:230px;background:radial-gradient(ellipse at 55% 50%,#c9cfc2,#f3f3f3 70%)}

/* services */
.services{top:1160px;height:440px;background:var(--dark)}
.svc-lead{position:absolute;left:170px;top:70px;width:260px}
.svc-lead h3{margin-top:22px;color:var(--white);font-size:24px;font-weight:700;line-height:28px}
.svc-lead p{margin-top:14px;color:#aaa;font-size:9px;line-height:13px}
.svc-lead .btn{position:relative;display:block;margin-top:18px;width:100px;height:24px;line-height:24px;font-size:10px}
.svc{position:absolute;width:240px;text-align:center;color:var(--white)}
.svc svg{display:block;margin:0 auto 8px}
.svc h4{font-size:10px;font-weight:700;letter-spacing:.3px}
.svc p{margin-top:5px;font-size:8.5px;line-height:12px;color:#aaa}

/* founder */
.founder{top:1600px;height:480px;background:linear-gradient(90deg,#2a2a30,#47464c 50%,#2a2a2f)}
.founder h3{position:absolute;left:190px;top:82px;color:var(--blue);font-size:22px;font-weight:700}
.founder p{position:absolute;left:190px;width:420px;color:#ccc;font-size:9.5px;line-height:14px}
.founder .btn{left:190px;top:286px;width:100px;height:26px;line-height:26px;font-size:10px}
.founder-photo{position:absolute;left:650px;top:50px;width:260px;height:430px;background:linear-gradient(180deg,#8a7f76,#3a3b45 45%,#1d2130)}
.founder .sig{position:absolute;left:830px;top:345px;font-family:"Great Vibes",cursive;color:var(--white);font-size:30px}
.founder .role{position:absolute;left:848px;top:390px;color:#ddd;font-size:10px}
.dots{position:absolute;left:190px;top:440px;display:flex;gap:6px}
.dots i{width:7px;height:7px;border-radius:50%;background:#777;display:block}
.dots i:first-child{background:var(--blue)}

/* partners */
.partners{top:2080px;height:180px;background:var(--white);display:flex;align-items:center;justify-content:center;gap:70px}
.partners span{font-size:24px;font-weight:700;color:#555;letter-spacing:1px}

/* footer */
.site-footer{top:2260px;height:428px;background:var(--darker);color:#bbb}
.foot-links{position:absolute;left:190px;top:60px;font-size:10px;line-height:44px;color:#ddd}
.contact{position:absolute;left:600px;top:130px;width:380px}
.contact h4{color:var(--white);font-size:14px;font-weight:600}
.contact p{margin-top:6px;font-size:9px;line-height:13px;color:#999}
.contact .line{margin-top:10px;font-size:9px;color:#bbb;display:flex;align-items:center;gap:8px}
.contact .line b{width:9px;height:9px;border-radius:50%;background:var(--blue);display:block}
.social{margin-top:14px;display:flex;gap:5px}
.social i{width:18px;height:18px;background:#3a3a3a;display:block}
.site-footer .btn{left:545px;top:330px;width:110px;height:22px;line-height:22px;font-size:10px}
.copy{position:absolute;top:392px;width:100%;text-align:center;font-size:8px;color:#777}
</style>
</head>
<body>

<header class="hero">
  <div class="hero-photo" role="img" aria-label="Business people meeting over coffee in a bright office"></div>
  <h1>WELL HELP MANAGE YOUR BUSINESS</h1>
  <p>Fast short term finance for small and medium businesses. Flexible funding, clear terms and quick approval so you can keep moving when opportunities appear.</p>
  <div class="btn">GET STARTED</div>
</header>

<nav class="topnav">
  <div class="brand"><i></i>Harbourline Funding</div>
  <div class="menu"><span>Home</span><span>Online Apply</span><span>Why Harbourline</span><span>Industries</span><span>About Us</span><span>Contact Us</span><span>Members Login</span></div>
</nav>

<section class="about">
  <div class="about-person" role="img" aria-label="Smiling businesswoman in a dark suit with arms crossed"></div>
  <h2>ABOUT US</h2>
  <p class="intro">Harbourline Funding provides short term finance solutions to businesses across many industries. Our team understands that cash flow moves fast, so we built a simple process with quick decisions and transparent terms. Whether you need working capital, equipment funding or support through a seasonal gap, we tailor each facility to your goals and stand beside you as a long term partner. We pride ourselves on trust, speed and clear communication from the first call to final repayment.</p>
  <div class="feature" style="left:490px;top:236px"><span class="ic"></span><h4>Grow your business</h4><p>Funding that helps you take on new work and expand with confidence.</p></div>
  <div class="feature" style="left:710px;top:236px"><span class="ic"></span><h4>Offering business loans</h4><p>Short term loans with flexible terms built around your cash flow.</p></div>
  <div class="feature" style="left:490px;top:318px"><span class="ic"></span><h4>Offering business loans</h4><p>Fast approvals and funds released quickly to keep you moving.</p></div>
  <div class="feature" style="left:710px;top:318px"><span class="ic"></span><h4>Boost your business</h4><p>Practical support and advice from a team that knows finance.</p></div>
  <div class="about-plant" role="img" aria-label="Hand holding a small green plant sprouting from soil"></div>
</section>

<section class="services">
  <div class="svc-lead">
    <svg width="90" height="80" viewBox="0 0 90 80"><path d="M45 4 L86 40 H74 V78 H16 V40 H4 Z" fill="#555"/><rect x="37" y="52" width="16" height="26" fill="#1b1b1b"/></svg>
    <h3>RESIDENTIAL REAL ESTATE AGENTS</h3>
    <p>We help agents bridge the gap between listing and settlement with fast access to commission advances, so your business keeps growing while deals close.</p>
    <span class="btn">Read More</span>
  </div>
  <div class="svc" style="left:560px;top:118px"><svg width="18" height="18" viewBox="0 0 18 18"><path d="M9 1 L17 9 H14 V17 H4 V9 H1 Z" fill="#fff"/></svg><h4>RESIDENTIAL REAL ESTATE AGENTS</h4><p>Advances on settled sales so agents can fund marketing and growth.</p></div>
  <div class="svc" style="left:830px;top:118px"><svg width="18" height="18" viewBox="0 0 18 18"><rect x="3" y="5" width="12" height="10" fill="#fff"/><rect x="7" y="1" width="4" height="4" fill="#fff"/></svg><h4>TELECOMMUNICATIONS</h4><p>Working capital for dealers and installers waiting on carrier payments.</p></div>
  <div class="svc" style="left:560px;top:218px"><svg width="18" height="18" viewBox="0 0 18 18"><rect x="2" y="10" width="3" height="7" fill="#fff"/><rect x="7" y="6" width="3" height="11" fill="#fff"/><rect x="12" y="2" width="3" height="15" fill="#fff"/></svg><h4>FINANCIAL PLANNERS</h4><p>Funding against trail and upfront fees to support practice growth.</p></div>
  <div class="svc" style="left:830px;top:218px"><svg width="18" height="18" viewBox="0 0 18 18"><rect x="1" y="4" width="16" height="12" fill="#fff"/><rect x="8" y="6" width="2" height="8" fill="#1b1b1b"/><rect x="5" y="9" width="8" height="2" fill="#1b1b1b"/></svg><h4>MEDICAL AND DENTAL EQUIPMENT</h4><p>Short term finance for suppliers while equipment orders are fulfilled.</p></div>
  <div class="svc" style="left:560px;top:318px"><svg width="18" height="18" viewBox="0 0 18 18"><rect x="1" y="3" width="16" height="10" fill="#fff"/><rect x="6" y="14" width="6" height="2" fill="#fff"/></svg><h4>OFFICE EQUIPMENT AND TECHNOLOGY AGENTS</h4><p>Cash flow support for agents selling office and technology products.</p></div>
  <div class="svc" style="left:830px;top:318px"><svg width="18" height="18" viewBox="0 0 18 18"><rect x="2" y="2" width="6" height="15" fill="#fff"/><rect x="10" y="6" width="6" height="11" fill="#fff"/></svg><h4>COMMERCIAL REAL ESTATE AGENTS</h4><p>Commission advances for leasing and sales agents on commercial deals.</p></div>
</section>

<section class="founder">
  <h3>DANIEL MARSH</h3>
  <p style="top:120px">Daniel founded Harbourline Funding after years in business banking, seeing first hand how good companies stall while waiting to be paid. He set out to build a lender that listens, decides quickly and treats every client as a partner.</p>
  <p style="top:200px">Under his leadership the team has supported hundreds of small and medium businesses with short term finance, always focused on fast action, honest advice and lasting relationships built on trust.</p>
  <span class="btn">Read More</span>
  <div class="founder-photo" role="img" aria-label="Portrait of the company founder in a dark suit"></div>
  <div class="sig">Daniel Marsh</div>
  <div class="role">Founder of Harbourline Funding</div>
  <div class="dots"><i></i><i></i><i></i></div>
</section>

<section class="partners">
  <span>NORTHWAY</span>
  <span>AVENLY</span>
  <span>CALDER STUDIO</span>
  <span>WESTGATE</span>
  <span>OSTREL</span>
</section>

<footer class="site-footer">
  <div class="foot-links"><div>Home</div><div>Partner</div><div>Privacy</div><div>Disclaimer</div></div>
  <div class="contact">
    <h4>Contact info</h4>
    <p>Speak with our team about fast short term finance for your business. We respond to every enquiry within one business day.</p>
    <div class="line"><b></b>Address: 14 Quay Street, Harbour City</div>
    <div class="line"><b></b>Email: hello@harbourline-funding.example</div>
    <div class="line"><b></b>Call: 000 555 0148</div>
    <div class="social"><i></i><i></i><i></i><i></i></div>
  </div>
  <span class="btn">Submit</span>
  <div class="copy">© Harbourline Funding. All rights reserved.</div>
</footer>

</body>
</html>
```